CD Cover Design Project

Project 2 CD cover design. One in English and one in Chinese. (I can provide the Chinese in PDF or any file if necessary.)
I will use the same design for 6 different CD cover with different title only. They all are related to my business-hypnosis.
I have Logo and the main content of the picture for you to design a cover.
I hope the whole design look like all while in a distance but only the title words show up. When you look closely you can see the design-the bird.
Will decide ASAP.
Target Market(s)
My students and audiences in hypnotist training courses.
Customer from my website and my hypnosis office.
Attendee in my lecture and conference.
Industry/Entity Type
Business
Requirements
Must have
- 1. It should looks close to white when been seen in a distance or first sight.
You can make my art work almost disappear or change to an idea like this Letter printing design.
Please visit:
http://zipzapblog-example.net/images/fruit_letterpress_macro.jpg
http://www.plumgrey-example.com/wp-content/uploads/2007/02/letterpress_2.jpg
2.About my logo.
Please use only the Bird sign but not the rest of the name and address.
Please have this information about the publisher on the other side:
"Self-hypnosis for Relaxation"
p.s. You can change the size and font and colour any way you wish.
This will be the other side of the cover.
Thank you.
CD Cover ,back, contain information-
Self-hypnosis for Relaxation
Benefits about Self hypnosis. You can fall back to sleep so much easier every night! Keeps a sense of logic and ease of mind every day. It gives you the control of your emotions and situations. You can apply it on daily business.
To help yourself to go into the deeper hypnotic trance easily you need to five yourself permission to dream, fantasize and play before allowing your rational mind to do the necessary job of sorting, assessing and figuring out hot to act upon the information that you receive. Many of us rationalize or criticize too quickly, without giving our intuition the time and space it deserve.
To give your self permission to use your imagination constructively and to open your mind and emotions to a newer ability, here are some suggestions for you to use. They are simple but powerful positive affirmations that gently help to alter your beliefs, habits and expectation toward your foal. When used on a regular basis is that they will help to make you more available for some experiences and less available for others. The power of this self-hypnosis is strong: what we ask for, we often receive.
Lie down with your back fully supported or sit comfortable in a quiet place.
Relax and breathe easily and deeply. Every time you breathe out, you feel more relaxed.
Count from 10 to 1, at each count you feel even more relax. At the last count, hold your breath and count for 3 seconds then let go, breathe out.
Read in your mind 10 times the following statement. In order not to full asleep, move your fingers while counting from the right hand to the left.
I’m calm. I’m relax. I’m in control.
ADD LOGO HERE
Willow Trance
www.willowtrance-example.com Ontario, Canada (905) 555-0143
- end -
Nice to have
- Clean and quiet, spiritual.
This is my both English and Chinese website. Please check it out even you might not read Chinese. All of the picture and art works are done by myself.
www.willowtrance-example.com
www.tw.willowtrance-example.com

```html
<!DOCTYPE html>
<html lang="en">
<head>
<meta charset="utf-8">
<title>Willow Trance – CD Cover Dieline</title>
<link href="https://fonts.googleapis.com/css2?family=Tinos:wght@400;700&family=Arimo:wght@400;700&family=PT+Sans&display=swap" rel="stylesheet">
<style>
  :root {
    --paper: #ffffff;
    --ink: #111111;
    --guide-bleed: #e8217f;
    --guide-trim: #2f9be6;
    --purple: #5b1f7e;
    --purple-deep: #47155f;
    --violet: #6a2c93;
    --lavender: #6b63b2;
    --frame: #b9b3dc;
    --blue-calm: #1f55c6;
    --blue-relax: #2f6fd2;
    --tagline-control: #4a165f;
    --slogan: #33338f;
    --spine-sky: #3f8ccd;
    --spine-navy: #2c2b86;
    --body-text: #4b3f63;
    --art-white: #fbfbfe;
    --art-haze: #eef0fa;
    --art-tint: #dfe3f4;
    --art-shadow: #d6d4e6;
  }
  * { box-sizing: border-box; margin: 0; padding: 0; }
  html, body { width: 1200px; height: 612px; overflow: hidden; background: var(--paper); }
  .canvas { position: relative; width: 1200px; height: 612px; background: var(--paper); }

  .template-label {
    position: absolute; left: 14px; top: 6px;
    font: 20px "PT Sans", sans-serif; color: #222;
  }
  .bleed-guide {
    position: absolute; left: 3px; top: 35px; width: 1193px; height: 546px;
    border: 1px dashed var(--guide-bleed);
  }
  .trim-guide {
    position: absolute; left: 10px; top: 42px; width: 1180px; height: 528px;
    border: 1.5px solid var(--guide-trim);
  }
  .fill-note {
    position: absolute; left: 0; width: 1240px; top: 590px; text-align: center;
    font: 15px "PT Sans", sans-serif; color: var(--guide-bleed);
  }

  /* near-white, letterpress-like artwork fields */
  .artwork {
    position: absolute; border: 1.5px solid var(--frame); border-radius: 3px;
    background:
      radial-gradient(ellipse at 42% 58%, var(--art-shadow) 0 12%, transparent 36%),
      linear-gradient(170deg, var(--art-white) 0%, var(--art-haze) 45%, var(--art-tint) 100%);
    box-shadow: inset 1px 1px 2px rgba(80, 70, 140, 0.12);
  }

  /* back panel */
  .back-panel { position: absolute; left: 10px; top: 42px; width: 575px; height: 528px; }
  .back-heading {
    position: absolute; left: 0; width: 575px; top: 26px; text-align: center;
    font: 700 18px "Tinos", serif; color: var(--purple); letter-spacing: 0.5px;
  }
  .tile-grid .artwork { width: 96px; height: 96px; }
  .guide-text {
    position: absolute; left: 272px; top: 66px; width: 262px;
    font: 10px/13px "Arimo", sans-serif; color: var(--body-text);
  }
  .guide-text .benefits { margin-bottom: 6px; }
  .guide-text ol { padding-left: 14px; }
  .guide-text li { margin-bottom: 3px; }
  .tagline {
    position: absolute; left: 0; width: 580px; top: 358px; text-align: center;
    font: 700 19px "Arimo", sans-serif;
  }
  .tagline .calm { color: var(--blue-calm); }
  .tagline .relax { color: var(--blue-relax); }
  .tagline .control { color: var(--tagline-control); }
  .publisher {
    position: absolute; left: 0; width: 580px; top: 402px; text-align: center;
    font: 14px/17px "Tinos", serif; color: var(--violet);
  }
  .publisher .catalog { font-weight: 700; color: var(--purple); font-size: 13px; margin-bottom: 2px; }
  .publisher .web { font-weight: 700; font-size: 11px; color: var(--purple); margin-top: 3px; }

  /* spine */
  .spine { position: absolute; left: 585px; top: 42px; width: 27px; height: 528px; }
  .spine .fold { position: absolute; top: 0; bottom: 0; border-left: 1.5px dashed var(--guide-trim); }
  .spine .band { position: absolute; left: 0; width: 27px; }
  .spine-title {
    position: absolute; left: 13px; top: 275px; transform: translate(-50%, -50%) rotate(90deg);
    white-space: nowrap; font: 700 13px "Tinos", serif; font-variant: small-caps; color: var(--ink);
    letter-spacing: 0.5px;
  }

  /* front panel */
  .front-panel { position: absolute; left: 612px; top: 42px; width: 578px; height: 528px; }
  .brand {
    position: absolute; left: 160px; top: 42px; display: flex; align-items: center; gap: 8px;
  }
  .brand-dot { width: 14px; height: 14px; border-radius: 50%; background: var(--ink); }
  .brand-name {
    font: 700 34px "Tinos", serif; font-variant: small-caps; color: var(--ink); line-height: 1;
  }
  .slogan {
    position: absolute; left: 0; width: 580px; top: 98px; text-align: center;
    font: 17px "Tinos", serif; letter-spacing: 3px; color: var(--slogan);
  }
  .front-panel .artwork { left: 163px; top: 130px; width: 254px; height: 337px; }
  .front-web {
    position: absolute; left: 0; width: 580px; top: 490px; text-align: center;
    font: 700 11px "Tinos", serif; color: var(--purple); letter-spacing: 0.5px;
  }
</style>
</head>
<body>
<main class="canvas">
  <div class="template-label">4 panel wrapcase - S</div>
  <div class="bleed-guide"></div>
  <div class="trim-guide"></div>

  <section class="back-panel">
    <h2 class="back-heading">Self-hypnosis for Relaxation</h2>
    <div class="tile-grid">
      <div class="artwork" style="left:60px;top:70px" role="img" aria-label="Faint near-white detail of the painted bird head"></div>
      <div class="artwork" style="left:164px;top:70px" role="img" aria-label="Faint near-white detail of the painted bird beak and eye"></div>
      <div class="artwork" style="left:60px;top:174px" role="img" aria-label="Faint near-white detail of the painted bird wing forms"></div>
      <div class="artwork" style="left:164px;top:174px" role="img" aria-label="Faint near-white detail of the painted bird body curves"></div>
    </div>
    <div class="guide-text">
      <p class="benefits">Fall back to sleep more easily every night. Keep a sense of logic and ease of mind every day. Gain control of your emotions and situations, and apply it in daily business.</p>
      <ol>
        <li>Lie down with your back fully supported, or sit comfortably in a quiet place.</li>
        <li>Relax and breathe easily and deeply. Every breath out, you feel more relaxed.</li>
        <li>Count from 10 to 1, more relaxed at each count. At the last, hold your breath for 3 seconds, then breathe out.</li>
        <li>Read the statement below in your mind 10 times, moving a finger at each count from right hand to left.</li>
      </ol>
    </div>
    <p class="tagline"><span class="calm">I’m calm</span> <span class="relax">I’m relax</span> <span class="control">I’m in control</span></p>
    <div class="publisher">
      <p class="catalog">EA-WT41270058</p>
      <p>Published by Willow Trance</p>
      <p>1450 Birchline Rd., Suite 310,</p>
      <p>Brookvale, ON K0A 9Z9</p>
      <p>(905) 555-0143</p>
      <p class="web">www.willowtrance-example.com</p>
    </div>
  </section>

  <section class="spine">
    <div class="band" style="top:0;height:33px;background:var(--lavender)"></div>
    <div class="band" style="top:33px;height:22px;background:var(--violet)"></div>
    <div class="band" style="top:55px;height:20px;background:var(--purple-deep)"></div>
    <div class="band" style="top:438px;height:35px;background:var(--purple-deep)"></div>
    <div class="band" style="top:473px;height:33px;background:var(--purple-deep)"></div>
    <div class="band" style="top:506px;height:15px;background:var(--spine-sky)"></div>
    <div class="band" style="top:521px;height:7px;background:var(--spine-navy)"></div>
    <div class="fold" style="left:0"></div>
    <div class="fold" style="left:26px"></div>
    <div class="spine-title">Willow Trance</div>
  </section>

  <section class="front-panel">
    <div class="brand">
      <span class="brand-dot"></span>
      <span class="brand-name">Willow Trance</span>
    </div>
    <p class="slogan">CREATE YOUR REALITY</p>
    <div class="artwork" role="img" aria-label="Near-white, embossed-style rendering of the painted bird in Northwest Coast style"></div>
    <p class="front-web">www.willowtrance-example.com</p>
  </section>

  <p class="fill-note">(fill the background of your artwork to the outside of the magenta line box)</p>
</main>
</body>
</html>
```